marketing flier needed - ONE SIDED

We are presently in the process of creating a marketing campaign, in which we will be distributing swag packs to our branches across the United States. These packs will include a range of items such as hats, shirts, beef jerky, peanuts, cups, and more. We require a marketing flier for internal use to inform our branch managers about this program. Our intention is to announce this program at the annual meeting. I kindly request the flier to be provided in digital format by January 21st, so that we can produce copies and send them out.

I will provide a mock-up of the flier that the CEO has prepared. As we are in the initial stages, we currently do not possess any images of the items. Additionally, I will also include the existing fliers that are currently being used.

Target Market(s)

roofers /construction workers

Industry/Entity Type

roofing materials construction

Font styles to use
Other font styles liked:
• does not matter - most of the customer are men so nothing girly

Colors
0054AA
0677BA
7BADD7
CADEEF
E8F1F8

Requirements
Must have
• a variety of marketing items with our logo

```html
<!DOCTYPE html>
<html lang="en">
<head>
<meta charset="UTF-8">
<title>Get The Swag! 2024 – Internal Flier</title>
<link href="https://fonts.googleapis.com/css2?family=Poppins:wght@400;500;800&display=swap" rel="stylesheet">
<style>
  :root {
    --navy: #263a82;
    --navy-deep: #22337a;
    --brand-blue: #0054AA;
    --sky-blue: #0677BA;
    --soft-blue: #7BADD7;
    --pale-blue: #CADEEF;
    --mist: #E8F1F8;
    --silver-light: #f4f5f7;
    --silver-mid: #c3c6cc;
    --silver-dark: #9a9ea6;
    --ink: #1f2f7a;
    --white: #ffffff;
    --page-bg: #f1f2f4;
  }
  * { box-sizing: border-box; margin: 0; padding: 0; }
  html, body { width: 1200px; height: 1200px; overflow: hidden; }
  body {
    background: var(--page-bg);
    font-family: 'Poppins', sans-serif;
    position: relative;
  }
  .flier {
    position: absolute;
    left: 207px; top: 49px;
    width: 786px; height: 1102px;
    overflow: hidden;
  }
  .flier-bg { position: absolute; inset: 0; }
  .notice {
    position: absolute; top: 22px; left: 0; width: 100%;
    text-align: center; margin-left: 4px;
    font-size: 35px; font-weight: 400; color: var(--ink);
    letter-spacing: 0.5px;
  }
  .brand {
    position: absolute; top: 140px; left: 0; width: 100%;
    display: flex; justify-content: center; align-items: center; gap: 12px;
    font-size: 24px; font-weight: 500; color: var(--ink);
  }
  .brand-dot {
    width: 22px; height: 22px; border-radius: 50%;
    background: var(--brand-blue);
  }
  .headline {
    position: absolute; top: 345px; left: 0; width: 100%;
    text-align: center;
    font-size: 92px; font-weight: 800; letter-spacing: -1px;
    background: linear-gradient(180deg, #ffffff 0%, #d9dbe0 45%, #a9adb5 60%, #eef0f3 100%);
    -webkit-background-clip: text; background-clip: text;
    color: transparent;
    filter: drop-shadow(3px 3px 0 #2b3c88);
  }
  .year-badge {
    position: absolute; left: 299px; top: 466px;
    width: 192px; height: 69px; border-radius: 16px;
    background: linear-gradient(135deg, #ffffff 0%, #c9ccd2 40%, #f2f3f5 65%, #a8acb3 100%);
    display: flex; align-items: center; justify-content: center;
    font-size: 56px; font-weight: 400;
    color: var(--sky-blue);
    line-height: 1;
  }
  .year-badge span {
    background: linear-gradient(90deg, var(--navy) 0%, var(--sky-blue) 100%);
    -webkit-background-clip: text; background-clip: text; color: transparent;
  }
  .swag-item {
    position: absolute; width: 160px; height: 160px; border-radius: 50%;
    background: var(--white);
    border: 6px solid var(--silver-mid);
    box-shadow: inset 0 0 0 2px #e6e7ea;
    display: flex; align-items: center; justify-content: center;
  }
  .swag-photo { display: block; }
  .item-hat   { left: 59px;  top: 566px; }
  .item-hat .swag-photo { width: 190px; height: 70px; border-radius: 60px 60px 30px 30px; background: #b07e56; }
  .item-jerky { left: 310px; top: 566px; }
  .item-jerky .swag-photo { width: 96px; height: 146px; border-radius: 6px; background: linear-gradient(180deg, #d2ab78 0%, #d2ab78 50%, #7a3c22 100%); }
  .item-box   { left: 553px; top: 566px; }
  .item-box .swag-photo { width: 180px; height: 100px; border-radius: 6px; background: linear-gradient(160deg, #ffffff, #dcdde0); }
  .item-mug   { left: 59px;  top: 747px; }
  .item-mug .swag-photo { width: 130px; height: 106px; border-radius: 10px 10px 28px 28px; background: linear-gradient(90deg, #ffffff, #dadbde); }
  .item-beanie { left: 310px; top: 747px; }
  .item-beanie .swag-photo { width: 108px; height: 120px; border-radius: 46px 46px 6px 6px; background: #9e9e9e; }
  .item-tee   { left: 553px; top: 747px; }
  .item-tee .swag-photo { width: 156px; height: 170px; border-radius: 10px; background: #f19a45; }
  .program-note {
    position: absolute; left: 32px; top: 985px;
    font-size: 19px; font-weight: 400; line-height: 29.5px;
    color: var(--white);
  }
</style>
</head>
<body>
  <main class="flier">
    <svg class="flier-bg" viewBox="0 0 786 1102" width="786" height="1102" aria-hidden="true">
      <defs>
        <linearGradient id="bodyGrad" x1="0" y1="0" x2="0" y2="1">
          <stop offset="0" stop-color="#263a82"/>
          <stop offset="0.55" stop-color="#0677BA"/>
          <stop offset="1" stop-color="#24408a"/>
        </linearGradient>
        <linearGradient id="topBlue" x1="0" y1="0" x2="1" y2="0">
          <stop offset="0" stop-color="#1a55a8"/>
          <stop offset="1" stop-color="#0677BA"/>
        </linearGradient>
        <linearGradient id="silverBand" x1="0" y1="0" x2="1" y2="0">
          <stop offset="0" stop-color="#b9bcc2"/>
          <stop offset="0.4" stop-color="#f3f4f6"/>
          <stop offset="1" stop-color="#a9adb4"/>
        </linearGradient>
        <linearGradient id="lowSilver" x1="0" y1="0" x2="1" y2="0">
          <stop offset="0" stop-color="#aeb1b8"/>
          <stop offset="0.5" stop-color="#eceef1"/>
          <stop offset="0.8" stop-color="#b9a7d6"/>
          <stop offset="1" stop-color="#d8dbe0"/>
        </linearGradient>
      </defs>
      <rect width="786" height="1102" fill="url(#bodyGrad)"/>
      <path d="M0 150 C120 290 330 375 520 360 C640 350 720 320 786 285 V340 C640 385 460 405 300 370 C170 340 70 290 0 235 Z" fill="url(#silverBand)"/>
      <path d="M0 0 H786 V280 C680 330 540 365 420 360 C250 352 110 280 0 200 Z" fill="url(#topBlue)"/>
      <path d="M52 0 H786 V120 C700 215 600 282 440 282 C280 282 140 200 52 0 Z" fill="#ffffff"/>
      <path d="M0 815 C40 920 110 955 260 958 C470 962 640 990 786 1060 V1102 H0 Z" fill="url(#lowSilver)"/>
      <path d="M0 815 C30 900 80 945 160 960 C120 955 60 960 0 965 Z" fill="#22337a"/>
      <path d="M0 975 C150 955 330 965 470 975 C620 988 720 1030 786 1075 V1102 H0 Z" fill="#283878"/>
    </svg>

    <p class="notice">* Internal Use Only *</p>
    <div class="brand"><span class="brand-dot"></span>Harborcrest Supply</div>

    <h1 class="headline">Get The Swag!</h1>
    <div class="year-badge"><span>2024</span></div>

    <div class="swag-item item-hat"><span class="swag-photo" role="img" aria-label="Brown fedora hat with company logo"></span></div>
    <div class="swag-item item-jerky"><span class="swag-photo" role="img" aria-label="Kraft pouch of beef jerky with company logo"></span></div>
    <div class="swag-item item-box"><span class="swag-photo" role="img" aria-label="White presentation swag box with company logo"></span></div>
    <div class="swag-item item-mug"><span class="swag-photo" role="img" aria-label="White coffee mug with company logo"></span></div>
    <div class="swag-item item-beanie"><span class="swag-photo" role="img" aria-label="Grey knit beanie with company logo"></span></div>
    <div class="swag-item item-tee"><span class="swag-photo" role="img" aria-label="Orange t-shirt with company logo"></span></div>

    <p class="program-note">Each branch will<br>get a quarterly shipment of “Swag”/logoed<br>items alongwith Presentation Swag Boxes to give out to customers.</p>
  </main>
</body>
</html>
```